Dutch craft distillery needs labels designed for Gin bottle

We are a small craft distillery based in The Netherlands. We are currently producing only GIN. While we do have a logo for our distillery, we are still in search of a winning design for our Gin bottle. We are looking for something modern yet classy. Let your creativity run wild. Play around with colours, think out of the box….The winning designer will be challenged to create the coolest labels for the different flavours of Gin we will be producing in the near future. The label will maintain the same design elements throughout the design, but will also be able to differentiate each variety clearly. So for e.g. A flowery Vantoor Gin can have a pink label with a different description and a spicy Vantoor gin can have another colour with another description and so on. If the design really appeals to us, we might also invite the designer to do our website for us!

In a nutshell: It is a 500 ml bottle, (Please check the attachment so you get an idea as to what kind of bottle to imagine while making the labels). The bottle is going to have a light coloured wooden lid/cork to it. As of now we have a transparent seal to complete the sealing process once the bottling is done. The idea is that we will have two labels. One in the front and one behind. The size of the labels are as follows:

Front label: 102 x 76 mm the front label. (TO BE USED HORIZONTALLY). The details that we need on the front label are in a separate attachment.

Back label: The size for the label at the back of the bottle is: 76 x 51 mm (TO BE USED VERTICALLY) The information that needs to come on the label behind is also in the same document which is attached separately. The label behind will also have batch no. & date (Please refer to attachment to understand what I mean by batch no. date, distiller’s signature etc.) I have attached a picture of an already existing brand which has its batch number and distillers signature etc on it….so you can understand what I exactly mean by that. Please do not copy their design, this is purely to give you an idea as to what I mean by batch number and so on. The address of the distillery can be put horizontally, vertically, on the side along one border, or however you find appropriate. This is the address:
Klaverhoekstraat 41,
6318 KT, Hengelo.
The Netherlands.
www.vantoor.nl

Logo’s no drinking when pregnant, No driving and drinking, No drinking under the age of 18 need to be present on the label behind. Alternately, we can also have www.calm-sipping.com instead of the under 18 no alcohol sign, most alcohol bottles these days have it. Please let me know what else you would need from me for this. So be creative and do your best!

Thanks and regards, Marisol Vendekampa.

Target Market(s)

Largely males and females between 25-55 , the audience could even be slightly older.

Colors

Designer to choose colors to be used in the design.

Requirements
Must have
• 1) The labels need to be modern, yet classy, elite..
• 2) We need to specify the fact that we are a craft distillery and the gin is HANDMADE, using only the highest quality ingredients.
• 3) We at Vantoor live, breathe, dream, talk about our dream which is our distillery and its product. The label needs to bring home this point and should clearly specify and mention that it is produced and bottled in The Netherlands. Or handmade and bottled with love and passion in The Netherlands or something to that effect if it matches with the rest of the design.
• 4) The colours you chose must match in some way or the other with the colours used for the logo design.
Nice to have
• Would be nice to have colours and look bold, although not completely necessary.
Should not have
• What I definitely do not want is something too whacky like a skull or some kind of vague work of art. For the rest, I leave it upto you….!

```html
<!DOCTYPE html>
<html lang="en">
<head>
<meta charset="utf-8">
<title>Vantoor Gin – Front Label</title>
<link rel="stylesheet" href="https://fonts.googleapis.com/css2?family=Rye&family=Libre+Baskerville:wght@400;700&family=Oswald:wght@400&display=swap">
<style>
  :root {
    --backdrop-light: #e6e8e3;
    --backdrop-dark: #b9bdb5;
    --label-black: #1c1c1c;
    --label-rib: #262626;
    --copper: #c8925a;
    --copper-dark: #8a5a32;
    --ivory: #f4efe6;
    --muted: #d9d4cb;
    --windmill-tone: #b8936a;
  }
  html, body {
    margin: 0;
    width: 785px;
    height: 1200px;
    overflow: hidden;
  }
  body {
    background: radial-gradient(ellipse at 50% 55%, var(--backdrop-light) 0%, var(--backdrop-dark) 100%);
    position: relative;
  }
  .front-label {
    position: absolute;
    left: 52px;
    top: 305px;
    width: 680px;
    height: 590px;
    background:
      repeating-linear-gradient(180deg, var(--label-black) 0 3px, var(--label-rib) 3px 5px);
    box-shadow: 0 6px 24px rgba(0,0,0,0.25);
  }
  .border-band {
    position: absolute;
    left: 0;
    right: 0;
    height: 28px;
    border-top: 2px solid var(--copper);
    border-bottom: 2px solid var(--copper);
  }
  .border-band::after {
    content: "";
    position: absolute;
    left: 0; right: 0;
    top: 10px;
    height: 4px;
    background: var(--copper-dark);
  }
  .border-band.top { top: 8px; }
  .border-band.bottom { bottom: 8px; }
  .side-rule {
    position: absolute;
    top: 40px;
    bottom: 40px;
    width: 2px;
    background: var(--copper-dark);
  }
  .side-rule.left { left: 8px; }
  .side-rule.right { right: 8px; }

  .centered {
    position: absolute;
    left: 0;
    right: 0;
    text-align: center;
  }
  .distillery-mark {
    top: 62px;
    font-family: "Libre Baskerville", serif;
    font-weight: 700;
    font-size: 17px;
    letter-spacing: 3px;
    color: var(--ivory);
    display: flex;
    justify-content: center;
    align-items: center;
    gap: 8px;
  }
  .distillery-mark .dot {
    width: 12px;
    height: 12px;
    border-radius: 50%;
    background: #c9452e;
  }
  .brand-name {
    top: 118px;
    font-family: "Rye", serif;
    font-size: 112px;
    line-height: 1;
    letter-spacing: 4px;
    color: var(--copper);
  }
  .spirit-name {
    top: 258px;
    font-family: "Libre Baskerville", serif;
    font-weight: 700;
    font-size: 82px;
    line-height: 1;
    color: var(--ivory);
  }
  .style-ribbon {
    position: absolute;
    left: 168px;
    top: 372px;
    width: 344px;
    height: 58px;
  }
  .style-ribbon span {
    position: absolute;
    left: 0; right: 0;
    top: 14px;
    text-align: center;
    font-family: "Oswald", sans-serif;
    font-size: 20px;
    letter-spacing: 0.5px;
    color: var(--label-black);
  }
  .producer-line {
    top: 436px;
    font-family: "Libre Baskerville", serif;
    font-size: 8px;
    letter-spacing: 0.5px;
    color: var(--muted);
  }
  .claims {
    top: 464px;
    font-family: "Libre Baskerville", serif;
    font-size: 13px;
    line-height: 20px;
    letter-spacing: 1px;
    color: var(--muted);
  }
  .volume {
    top: 520px;
    font-family: "Libre Baskerville", serif;
    font-size: 15px;
    letter-spacing: 1px;
    color: var(--ivory);
  }
  .origin {
    top: 543px;
    font-family: "Libre Baskerville", serif;
    font-size: 7px;
    letter-spacing: 0.5px;
    color: var(--muted);
  }
  .craft-seal {
    position: absolute;
    left: 22px;
    top: 362px;
    width: 94px;
    height: 94px;
    border-radius: 50%;
    background: var(--copper-dark);
    border: 3px solid var(--copper);
    box-sizing: border-box;
  }
  .windmill-art {
    position: absolute;
    left: 505px;
    top: 300px;
    width: 160px;
    height: 210px;
    background: linear-gradient(180deg, rgba(184,147,106,0.15) 0%, rgba(184,147,106,0.55) 100%);
  }
</style>
</head>
<body>
  <section class="front-label" aria-label="Vantoor Gin front label">
    <div class="border-band top"></div>
    <div class="border-band bottom"></div>
    <div class="side-rule left"></div>
    <div class="side-rule right"></div>

    <div class="centered distillery-mark"><span class="dot"></span>VANTOOR DISTILLERY</div>
    <div class="centered brand-name">VANTOOR</div>
    <div class="centered spirit-name">GIN</div>

    <div class="style-ribbon">
      <svg width="344" height="58" viewBox="0 0 344 58" aria-hidden="true">
        <polygon points="0,22 34,22 34,52 0,52 14,37" fill="#bdb6aa"/>
        <polygon points="344,22 310,22 310,52 344,52 330,37" fill="#bdb6aa"/>
        <rect x="24" y="8" width="296" height="36" fill="#f4efe6" stroke="#1c1c1c" stroke-width="1.5"/>
      </svg>
      <span>PREMIUM LONDON DRY GIN</span>
    </div>

    <div class="centered producer-line">DISTILLED AND BOTTLED BY VANTOOR DISTILLERY</div>
    <div class="centered claims">100% NATURAL BOTANICALS<br>NO ARTIFICIAL FLAVOURING</div>
    <div class="centered volume">50 CL | 43% VOL</div>
    <div class="centered origin">PRODUCT OF THE NETHERLANDS</div>

    <div class="craft-seal" aria-hidden="true"></div>
    <div class="windmill-art" role="img" aria-label="Line illustration of a Dutch windmill with tulips"></div>
  </section>
</body>
</html>
```